chocolate bar wrapper

Need a design for a new line of chocolate bars being sold at new retail candy store concept called PLINKTREATS. There will be many flavors including Dark Chocolate, Milk Chocolate, Dark Chocolate Espresso, Milk Chocolate Smores, Dark Chocolate Strawberry Champagne, Dark Chocolate Sea Salt, Dark Chocolate Chipotle, etc. Size of bar is 3 inches x 6 5/8 inches.

Please visit PLINKTREATS.EXAMPLE

Industry/Entity Type

Retail

```html
<!DOCTYPE html>
<html lang="en">
<head>
<meta charset="UTF-8">
<title>Dark Chocolate Strawberry Champagne Wrapper</title>
<link rel="stylesheet" href="https://fonts.googleapis.com/css2?family=Almendra:wght@400&display=swap">
<style>
  :root {
    --stage: #000000;
    --wrapper-pink: #ee5068;
    --rule-white: #ffffff;
    --chocolate: #744b2a;
    --chocolate-drip: #6a4222;
    --berry-top: #f6766f;
    --berry-bottom: #e85d7b;
    --glass-tint: #f7c9d0;
  }
  * { margin: 0; padding: 0; box-sizing: border-box; }
  html, body {
    width: 1200px;
    height: 997px;
    overflow: hidden;
    background: var(--stage);
  }
  .canvas {
    position: relative;
    width: 1200px;
    height: 997px;
    background: var(--stage);
  }
  .wrapper {
    position: absolute;
    left: 366px;
    top: 22px;
    width: 418px;
    height: 946px;
    background: var(--wrapper-pink);
    overflow: hidden;
  }
  .glass-illustration {
    position: absolute;
    left: 165px;
    top: 143px;
    width: 86px;
    height: 275px;
    background: var(--glass-tint);
    border-radius: 4px;
  }
  .title-band {
    position: absolute;
    left: 0;
    top: 474px;
    width: 100%;
    height: 115px;
    border-top: 5px solid var(--rule-white);
    border-bottom: 5px solid var(--rule-white);
    text-align: center;
    color: var(--rule-white);
    font-family: "Almendra", serif;
  }
  .flavor-line {
    font-size: 47px;
    line-height: 1;
    margin-top: 10px;
    letter-spacing: 0.5px;
  }
  .flavor-sub {
    font-size: 30px;
    line-height: 1;
    margin-top: 6px;
  }
  .chocolate-band {
    position: absolute;
    left: 0;
    top: 589px;
    width: 100%;
    height: 218px;
    background: var(--chocolate);
  }
  .berry-band {
    position: absolute;
    left: 0;
    top: 805px;
    width: 100%;
    height: 141px;
    background: linear-gradient(to bottom, var(--berry-top), var(--berry-bottom));
  }
  .drip-edge {
    position: absolute;
    left: 0;
    top: 798px;
    width: 418px;
    height: 28px;
  }
</style>
</head>
<body>
<main class="canvas">
  <section class="wrapper">
    <div class="glass-illustration" role="img" aria-label="White champagne flute silhouette"></div>

    <header class="title-band">
      <h1 class="flavor-line">Dark Chocolate</h1>
      <p class="flavor-sub">Strawberry Champagne</p>
    </header>

    <div class="chocolate-band"></div>

    <div class="berry-band" role="img" aria-label="Bubbly strawberry champagne layer"></div>

    <svg class="drip-edge" viewBox="0 0 418 28" aria-hidden="true">
      <path fill="var(--chocolate)" d="M0 0 H418 V10 C400 12 390 8 372 10 C350 13 335 9 310 11 C290 13 280 18 265 12 C240 8 220 12 195 10 C170 9 150 12 130 10 C110 8 95 4 75 9 C55 12 30 9 0 11 Z"/>
      <path fill="var(--chocolate-drip)" d="M75 9 C88 2 105 3 118 8 C104 7 90 7 75 9 Z M300 11 C315 4 335 5 348 10 C332 9 316 10 300 11 Z"/>
    </svg>
  </section>
</main>
</body>
</html>
```